Unique Beautiful Realtor business card

I need a unique business card that includes my logo, my firms logo, my picture and phone number. The colors should compliment my logo.

Target Market(s)

People who want to buy or sell a home in South Florida

Contact Information for Business Card

Use two sides and work with the DRM Coastal Homes logo as a theme.
The Harlow Benton should be small and discreet, it is a requirement to be there but should be small. My photo should be integrated artistically.

Font styles to use
Serif
Sans Serif

Colors

Designer to choose colors to be used in the design.

Requirements
Must have
• My logo, Harlow Benton logo, my photo, my phone number, (954-283-6091) and my website address. (www.drmcoastalhomes.example)
• Also my name, Dana R. Moreland, PA, Realtor
• Also “The Pet Friendly Realtor”

```html
<!DOCTYPE html>
<html lang="en">
<head>
<meta charset="utf-8">
<title>Dana R. Moreland – Business Card</title>
<link href="https://fonts.googleapis.com/css2?family=Michroma&family=Lato:wght@400;700&display=swap" rel="stylesheet">
<style>
  :root {
    --navy: #1b4a86;
    --olive: #a3a614;
    --palm-green: #9fae1e;
    --text-grey: #444a52;
    --card-white: #ffffff;
    --backdrop: #ecebe8;
    --photo-dark: #4a4d55;
    --photo-light: #c9a877;
  }
  * { box-sizing: border-box; margin: 0; padding: 0; }
  html, body { width: 1200px; height: 900px; overflow: hidden; }
  body { background: var(--backdrop); position: relative; font-family: "Lato", sans-serif; }

  .card { position: absolute; background: var(--card-white); overflow: hidden; }
  .card--front { left: 330px; top: 90px; width: 555px; height: 343px; }
  .card--back  { left: 330px; top: 469px; width: 558px; height: 343px; }

  .palm-art {
    position: absolute; left: 0; top: 0; width: 190px; height: 343px;
    background: linear-gradient(160deg, var(--palm-green) 0%, rgba(159,174,30,0.55) 40%, rgba(27,74,134,0.7) 100%);
    clip-path: polygon(0 0, 100% 0, 100% 25%, 30% 45%, 8% 100%, 0 100%);
  }

  .agent-photo {
    position: absolute; left: 335px; top: 100px; width: 220px; height: 233px;
    background: linear-gradient(180deg, var(--photo-light) 0%, var(--photo-dark) 55%);
    border-radius: 90px 90px 0 0;
  }

  .details { position: absolute; left: 75px; top: 174px; width: 250px; z-index: 1; }

  .agent-name {
    font-family: "Michroma", sans-serif; font-size: 15px; line-height: 20px;
    color: var(--navy); letter-spacing: 0.3px; white-space: nowrap;
  }
  .agent-title { font-size: 15px; line-height: 18px; color: var(--text-grey); margin-left: 1px; }

  .contact { list-style: none; margin-top: 16px; margin-left: 1px; font-size: 15px; color: var(--text-grey); }
  .contact li { display: flex; align-items: center; gap: 5px; height: 21px; white-space: nowrap; }
  .contact svg { width: 14px; height: 14px; fill: var(--navy); flex: none; }

  .brokerage {
    display: flex; align-items: center; gap: 8px; margin-top: 16px; margin-left: 1px;
    font-size: 15px; font-weight: 700; color: var(--text-grey);
  }
  .brokerage .mark { width: 14px; height: 14px; background: #b5203a; }

  .front-band { position: absolute; left: 0; bottom: 0; width: 100%; height: 9px; background: var(--navy); }

  .brand-mark {
    position: absolute; left: 0; top: 0; width: 100%; height: 300px;
    display: flex; align-items: center; justify-content: center;
  }
  .brand-name {
    font-family: "Michroma", sans-serif; font-size: 26px; color: var(--navy); letter-spacing: 1px;
  }
  .tagline-band {
    position: absolute; left: 0; bottom: 0; width: 100%; height: 38px; background: var(--olive);
    display: flex; align-items: center; justify-content: center;
    color: #fff; font-size: 16px; letter-spacing: 0.3px;
  }
</style>
</head>
<body>
  <section class="card card--front">
    <div class="palm-art" role="img" aria-label="Stylised palm tree illustration"></div>
    <div class="agent-photo" role="img" aria-label="Portrait photo of the realtor in a grey blazer"></div>
    <div class="details">
      <h1 class="agent-name">DANA R. MORELAND</h1>
      <p class="agent-title">PA, Realtor</p>
      <ul class="contact">
        <li>
          <svg viewBox="0 0 24 24" aria-hidden="true"><path d="M6.6 10.8a15.1 15.1 0 0 0 6.6 6.6l2.2-2.2a1 1 0 0 1 1-.25 11.4 11.4 0 0 0 3.6.57 1 1 0 0 1 1 1V20a1 1 0 0 1-1 1A17 17 0 0 1 3 4a1 1 0 0 1 1-1h3.5a1 1 0 0 1 1 1c0 1.25.2 2.45.57 3.57a1 1 0 0 1-.25 1z"/></svg>
          954-283-6091
        </li>
        <li>
          <svg viewBox="0 0 24 24" aria-hidden="true"><path d="M12 2a10 10 0 1 0 0 20 10 10 0 0 0 0-20zm6.9 6h-2.9a15.7 15.7 0 0 0-1.4-3.6A8 8 0 0 1 18.9 8zM12 4c.8 1.2 1.5 2.5 1.9 4h-3.8c.4-1.5 1.1-2.8 1.9-4zM4.3 14a8 8 0 0 1 0-4h3.4a16 16 0 0 0 0 4zm.8 2h2.9c.3 1.3.8 2.5 1.4 3.6A8 8 0 0 1 5.1 16zM8 8H5.1a8 8 0 0 1 4.3-3.6C8.8 5.5 8.4 6.7 8 8zm4 12c-.8-1.2-1.5-2.5-1.9-4h3.8c-.4 1.5-1.1 2.8-1.9 4zm2.3-6H9.7a14.6 14.6 0 0 1 0-4h4.6a14.6 14.6 0 0 1 0 4zm.3 5.6c.6-1.1 1.1-2.3 1.4-3.6h2.9a8 8 0 0 1-4.3 3.6zM16.3 14a16 16 0 0 0 0-4h3.4a8 8 0 0 1 0 4z"/></svg>
          www.drmcoastalhomes.example
        </li>
      </ul>
      <div class="brokerage"><span class="mark"></span>Harlow Benton</div>
    </div>
    <div class="front-band"></div>
  </section>

  <section class="card card--back">
    <div class="brand-mark"><span class="brand-name">DRM COASTAL HOMES</span></div>
    <div class="tagline-band">THE PET FRIENDLY REALTOR</div>
  </section>
</body>
</html>
```